Product Label & Logo for New Supplement

Your design will automatically be eliminated if you do NOT read this brief, because the description tells you about the brand you will be creating an identity for.Attached is the current label for the product. It is boring and doesn’t tell a story.We need you to unleash creative work to help patients with chronic pain diseases - like Multiple Sclerosis, Chronic Fatigue Syndrome, Lupus, and Fibromyalgia - no longer be defined by their disease. Velq Tonic is a new supplement developed by a neurologist to help patients with chronic pain feel better and have better days. It increases energy and stamina, saving the patient from having to take upwards of 40 different supplements.The label and logo need to convey that this supplement will give hurting patients new life.
Updates
Target Market(s)
People with fatigue, pain and inflammation
Industry/Entity Type
Supplement
Requirements
Must have
- Gender neutral, eye catching, all the ingredients listed in addition to logo design
Nice to have
- Custom logo, no generic fonts for name brand

```html
<!DOCTYPE html>
<html lang="en">
<head>
<meta charset="utf-8">
<title>Velq Tonic – Supplement Label</title>
<link href="https://fonts.googleapis.com/css2?family=Audiowide&display=swap" rel="stylesheet">
<style>
  :root {
    --stage: #1c1c1c;
    --ink: #3d1890;
    --violet-deep: #3a1a8c;
    --violet: #7b3fd6;
    --purple: #9a4fe0;
    --lilac: #c79af0;
    --sky: #5f8fe0;
    --glow: #f4f1ff;
  }
  * { margin: 0; padding: 0; box-sizing: border-box; }
  html, body {
    width: 1200px;
    height: 787px;
    overflow: hidden;
    background: var(--stage);
  }
  .label {
    position: absolute;
    left: 286px;
    top: 0;
    width: 628px;
    height: 787px;
    overflow: hidden;
    font-family: "Audiowide", sans-serif;
    color: var(--ink);
  }
  .label__art {
    position: absolute;
    inset: 0;
    background:
      linear-gradient(118deg, rgba(0,0,0,0) 34%, rgba(205,160,245,0.55) 42%, rgba(160,90,230,0.65) 50%, rgba(205,160,245,0.5) 58%, rgba(0,0,0,0) 66%),
      radial-gradient(ellipse 40% 22% at 72% 62%, var(--glow) 0%, rgba(244,241,255,0) 75%),
      radial-gradient(ellipse 45% 18% at 80% 38%, rgba(255,255,255,0.75) 0%, rgba(255,255,255,0) 75%),
      radial-gradient(ellipse 40% 30% at 8% 70%, rgba(160,80,230,0.8) 0%, rgba(160,80,230,0) 75%),
      linear-gradient(160deg, var(--sky) 0%, var(--violet) 36%, var(--lilac) 55%, var(--purple) 78%, var(--violet-deep) 100%);
  }
  .band {
    position: absolute;
    left: 0;
    width: 100%;
    background: linear-gradient(90deg, rgba(255,255,255,0.72), rgba(255,255,255,0.5) 50%, rgba(255,255,255,0.72));
  }
  .band--top { top: 68px; height: 102px; }
  .band--bottom { top: 586px; height: 94px; }
  .brand {
    position: absolute;
    display: flex;
    align-items: center;
    line-height: 1;
    white-space: nowrap;
  }
  .brand__dot {
    flex: none;
    border-radius: 50%;
    background: var(--ink);
  }
  .brand--small { left: 44px; top: 100px; gap: 10px; font-size: 32px; }
  .brand--small .brand__dot { width: 26px; height: 26px; }
  .brand--large { left: 34px; top: 326px; gap: 12px; font-size: 90px; }
  .brand--large .brand__dot { width: 44px; height: 44px; }
  .claim {
    position: absolute;
    left: 384px;
    top: 84px;
    font-size: 21px;
    line-height: 24px;
    text-transform: uppercase;
  }
  .category {
    position: absolute;
    left: 34px;
    top: 603px;
    font-size: 21px;
    line-height: 24px;
    text-transform: uppercase;
  }
  .count {
    position: absolute;
    left: 424px;
    top: 627px;
    font-size: 21px;
    line-height: 24px;
    text-transform: uppercase;
  }
</style>
</head>
<body>
  <main class="label">
    <div class="label__art" role="img" aria-label="Glowing purple and blue DNA double helix rising diagonally across a bright blue-white sky"></div>
    <div class="band band--top"></div>
    <div class="band band--bottom"></div>

    <div class="brand brand--small"><span class="brand__dot"></span><span>Velq Tonic</span></div>
    <p class="claim">Help patients<br>with chronic<br>pain diseases</p>

    <h1 class="brand brand--large"><span class="brand__dot"></span><span>Velq Tonic</span></h1>

    <p class="category">Dietary<br>supplement</p>
    <p class="count">60 tablets</p>
  </main>
</body>
</html>
```